Market place for used airplanes/helicopters/parts

http://www.vingtorget.se needs a facelift.

# What is it
Classifieds for used airplanes/helicopters/parts/spare parts/aviation literature, for people in Scandinavia. The number of classifieds is ~120-200. They are mainly in Swedish, English, Norwegian.

It's not a glamorous or luxurious business, but more for people with a genuine interest in flying, technical things.

Similar to sites like this, but they have much more classifieds than my site
http://www.skyquarry.com/list/list.aspx?ETID=1&setype=1&catid=6
http://www.lindqvistflyg.com/planes.asp?meny=1&typ=single
https://www.propwashdeals.com/cat.php?mode=listing&main=

# What I want
Design only - no code. I want a modern, maybe a bit bootstrap like, clean, simple, not flashy, web design. I want the design to be in English.

# Audience of the website
Aviation interested men, 45-65 years old, in the nordic countries (around Sweden).

# Logotype that could be used (but not necessarily)
http://www.vingtorget.se/flygplan_till_salu_large.jpg
http://www.vingtorget.se/flygplan_till_salu.eps

Reason: I decided to extend the deadline with 1 day. The reason is that I (unfortunately) managed to put the contest in the wrong category for 1 day + I want to give you all feedback (been too busy the whole day, sorry).

Hi all! 

Thanks everyone for the contributions you made. 

I will setup a poll for the designs that I like most. Will get back when I have more information. 

Thanks and have a nice weekend!
Kjell

Target Market(s)

45-65 old Scandinavian men

Industry/Entity Type

Business

Requirements
Must have
• - A list with classifieds on the first page, so the visitor easily can see new classifieds.
- A classifieds should be able to have more than one photo
- A simple navigation for showing classifieds from categories like airplanes, helicopters/gyrocopters, parts, literature, misc (maybe other categories) .... but still, it's just 100-200 ads so it's not needed that much filtration.

- A placeholder/way of showing aviation news/clips. In the old design I had, it was a column to the right. It's enough to show maybe 2-5 placeholders.
- A placeholder for PlaceAds ads somewhere on the site.
Should not have
• - Carousels
- Too much clutter

```html
<!DOCTYPE html>
<html lang="en">
<head>
<meta charset="utf-8">
<title>Vingtorget – Aircraft Classifieds</title>
<link href="https://fonts.googleapis.com/css2?family=Amaranth&family=Oswald:wght@500&family=Open+Sans:wght@400;600&family=Ubuntu:wght@500&family=Montserrat:wght@400&display=swap" rel="stylesheet">
<style>
:root{
  --blue:#0b5aa0;
  --blue-dark:#0a4f8d;
  --blue-light:#1a9fd8;
  --blue-text:#1470b8;
  --orange:#f26a1b;
  --orange-light:#ff8a3a;
  --grey-bg:#f3f3f3;
  --border:#d9d9d9;
  --text:#333;
  --muted:#666;
}
*{box-sizing:border-box;margin:0;padding:0}
html,body{width:863px;height:1200px;overflow:hidden;background:#fff}
body{position:relative;font-family:"Open Sans",Arial,sans-serif;color:var(--text);font-size:11px}
.abs{position:absolute}
a{color:inherit;text-decoration:none}

/* header */
.site-header{left:0;top:0;width:863px;height:79px;border-top:2px solid var(--blue);background:linear-gradient(#fff,#eee)}
.brand{left:95px;top:28px;display:flex;align-items:center;gap:8px;font-family:"Ubuntu",sans-serif;font-weight:500;font-size:24px;color:var(--blue)}
.brand-mark{width:14px;height:14px;background:var(--blue);border-radius:50%}
.btn-top{top:11px;height:26px;border-radius:4px;color:#fff;font-family:"Ubuntu",sans-serif;font-weight:500;font-size:13px;display:flex;align-items:center;justify-content:center;border:1px solid #0b4a7f}
.btn-submit{left:546px;width:120px;background:linear-gradient(#1577b8,#0b5a98)}
.btn-edit{left:673px;width:95px;background:linear-gradient(#2bb4f0,#1490d6);border-color:#1a8ccc}
.main-nav{left:455px;top:50px;display:flex;font-family:"Montserrat",sans-serif;font-size:10.5px;text-transform:uppercase}
.main-nav a{height:19px;display:flex;align-items:center;justify-content:center;color:#222}
.main-nav a.active{background:var(--blue);color:#fff;border-radius:2px}

.hero{left:0;top:79px;width:863px;height:122px;background:linear-gradient(180deg,#6d8a4b 0%,#9bb56a 45%,#8a4a32 60%,#a8c07c 100%)}

/* sidebar */
.side-box{left:94px;width:122px;background:var(--grey-bg);box-shadow:0 4px 4px -2px rgba(0,0,0,.18)}
.side-head{height:31px;background:linear-gradient(#2cb3e4,#1690c9);color:#fff;font-family:"Oswald",sans-serif;font-weight:500;font-size:17px;padding:3px 0 0 10px;letter-spacing:.3px}
.cat-list{list-style:none;padding:6px 14px 0 14px}
.cat-list li{height:23.5px;border-bottom:1px solid #e2e2e2;display:flex;align-items:center;gap:9px;color:var(--blue-text);font-size:10px}
.cat-list li::before{content:"";width:6px;height:6px;border:1px solid #aaa;background:#fff}
.view-all{display:flex;align-items:center;gap:6px;color:var(--orange);font-size:9px}
.view-all svg{width:9px;height:9px}
.news-item{padding:0 10px;margin-top:13px}
.news-item h3{font-family:"Open Sans",sans-serif;font-weight:400;color:var(--blue-text);font-size:11px;margin-bottom:3px}
.news-item p{font-size:9.5px;line-height:12.5px;color:#222}

/* listings */
.listing{left:229px;width:426px;height:132px;border:1px solid var(--border);background:#f7f7f7}
.thumbs{position:absolute;left:11px;top:11px;display:flex;gap:10px}
.thumb{width:68px;height:52px;border:1px solid #ccc}
.listing h2{position:absolute;left:9px;top:70px;font-family:"Amaranth",sans-serif;font-weight:400;font-size:16px;color:var(--blue-dark)}
.listing .desc{position:absolute;left:9px;top:96px;width:270px;font-size:9.5px;line-height:13px;color:#333}
.meta{position:absolute;left:294px;top:8px;font-size:9.5px;line-height:16px}
.meta dt{display:inline;color:var(--blue-text)}
.meta dd{display:inline;color:#222}
.share{position:absolute;left:294px;top:60px;display:flex;align-items:center;gap:6px;color:var(--blue-text);font-size:9.5px}
.share span.ico{width:17px;height:16px;border-radius:2px}
.btn-more{position:absolute;left:293px;top:102px;width:111px;height:18px;border-radius:3px;background:linear-gradient(var(--orange-light),var(--orange));color:#fff;font-size:9.5px;display:flex;align-items:center;justify-content:center;gap:5px}
.btn-more svg{width:8px;height:8px}

/* ads */
.ad{left:667px;width:102px;border:1px solid #555}

/* footer */
.footer-band{left:0;top:980px;width:863px;height:220px;background:var(--blue)}
.footer-panel{left:94px;top:972px;width:674px;height:210px;background:linear-gradient(#fafafa,#e9e9e9);border-radius:0 0 40px 40px / 0 0 10px 10px}
.footer-panel::before,.footer-panel::after{content:"";position:absolute;top:0;width:60px;height:40px;background:#fff}
.footer-title{font-family:"Amaranth",sans-serif;font-size:17px;color:#e2621a}
.footer-text{font-size:10px;line-height:14px;color:#333}
.newsletter-form{left:121px;top:1086px;display:flex;height:25px}
.newsletter-form input{width:161px;height:25px;border:none;border-bottom:1px solid #ccc;padding-left:7px;font-family:"Times New Roman",serif;font-size:10px;color:#333;background:#fff}
.newsletter-form button{width:66px;height:25px;border:none;background:linear-gradient(var(--orange-light),var(--orange));color:#fff;font-family:"Amaranth",sans-serif;font-size:13px;display:flex;align-items:center;justify-content:center;gap:6px}
.quick-links{left:558px;top:1035px;display:flex;font-size:10px;color:#333}
.quick-links a+a{border-left:1px solid #bbb;margin-left:8px;padding-left:8px}
.social{left:558px;top:1062px;display:flex;gap:12px}
.social span{width:27px;height:27px;border-radius:4px}
.copyright{left:94px;top:1137px;width:674px;text-align:center;font-size:9.5px;color:#555}
.footer-rule{left:108px;top:1126px;width:646px;border-top:1px solid #cfcfcf}
</style>
</head>
<body>

<header class="site-header abs">
  <div class="brand abs" style="top:26px"><span class="brand-mark"></span>VINGTORGET</div>
  <a class="btn-top btn-submit abs" href="#">Submit a Classified</a>
  <a class="btn-top btn-edit abs" href="#">Edit Classified</a>
  <nav class="main-nav abs">
    <a class="active" href="#" style="width:56px">Home</a>
    <a href="#" style="width:106px">About Us</a>
    <a href="#" style="width:44px">FAQ</a>
    <a href="#" style="width:120px">Contact Us</a>
  </nav>
</header>

<div class="hero abs" role="img" aria-label="Banner photo of vintage biplanes parked on a grass airfield"></div>

<aside class="side-box abs" style="top:215px;height:211px">
  <div class="side-head">CATEGORY</div>
  <ul class="cat-list">
    <li>Airplanes</li><li>Helicopters</li><li>Gyrocopters</li><li>Parts</li><li>Literature</li><li>Misc</li>
  </ul>
  <a class="view-all" href="#" style="margin:15px 0 0 16px"><svg viewBox="0 0 10 10"><circle cx="5" cy="5" r="4.2" fill="none" stroke="#f26a1b"/><path d="M4 3l2 2-2 2" fill="none" stroke="#f26a1b"/></svg>View All</a>
</aside>

<aside class="side-box abs" style="top:441px;height:282px">
  <div class="side-head">LATEST NEWS</div>
  <div class="news-item"><h3>Lorem Ipsum simply</h3><p>Lorem ipsum is simply dummy text of the printing...</p></div>
  <div class="news-item"><h3>Lorem Ipsum simply</h3><p>Lorem ipsum is simply dummy text of the printing...</p></div>
  <div class="news-item"><h3>Lorem Ipsum simply</h3><p>Lorem ipsum is simply dummy text of the printing...</p></div>
  <a class="view-all" href="#" style="margin:16px 0 0 10px"><svg viewBox="0 0 10 10"><circle cx="5" cy="5" r="4.2" fill="none" stroke="#f26a1b"/><path d="M4 3l2 2-2 2" fill="none" stroke="#f26a1b"/></svg>View All</a>
</aside>

<main>
  <article class="listing abs" style="top:214px">
    <div class="thumbs">
      <div class="thumb" role="img" aria-label="Aircraft photo" style="background:linear-gradient(#9fb7cf,#b33 60%,#6a8a45)"></div>
      <div class="thumb" role="img" aria-label="Aircraft photo" style="background:linear-gradient(#5a5a5a,#eee 50%,#777)"></div>
      <div class="thumb" role="img" aria-label="Aircraft photo" style="background:linear-gradient(#4d6a7e,#cfe2ea 55%,#3b7a8e)"></div>
    </div>
    <h2>Norrvinge NV-12</h2>
    <p class="desc">En unik UL-maskin i kolfiber, det gör den exceptionellt lätt. Tomvikt 68kg Tillv. 2006, ca.260 timmar, alltid hangar....</p>
    <dl class="meta"><dt>Namn:</dt> <dd>Nils Berglund</dd><br><dt>Telefon:</dt> <dd>+46 700 00 12 34</dd><br><dt>Datum:</dt> <dd>2013-10-04 16:49:39</dd></dl>
    <div class="share">Share on <span class="ico" style="background:#3b5b9a;margin-left:6px"></span><span class="ico" style="background:#3aa4e0"></span></div>
    <a class="btn-more" href="#">View More Details <svg viewBox="0 0 10 10"><circle cx="5" cy="5" r="4.2" fill="none" stroke="#fff"/><path d="M4 3l2 2-2 2" fill="none" stroke="#fff"/></svg></a>
  </article>

  <article class="listing abs" style="top:359px">
    <div class="thumbs">
      <div class="thumb" role="img" aria-label="Aircraft photo" style="background:linear-gradient(#6c8c4a,#e9e9e9 55%,#5f7f3f)"></div>
      <div class="thumb" role="img" aria-label="Aircraft photo" style="background:linear-gradient(#c8a030,#c33 55%,#7a8a60)"></div>
      <div class="thumb" role="img" aria-label="Aircraft photo" style="background:linear-gradient(#c9c9c9,#c22 55%,#888)"></div>
    </div>
    <h2>Norrvinge NV-12</h2>
    <p class="desc">En unik UL-maskin i kolfiber, det gör den exceptionellt lätt. Tomvikt 68kg Tillv. 2006, ca.260 timmar, alltid hangar....</p>
    <dl class="meta"><dt>Namn:</dt> <dd>Nils Berglund</dd><br><dt>Telefon:</dt> <dd>+46 700 00 12 34</dd><br><dt>Datum:</dt> <dd>2013-10-04 16:49:39</dd></dl>
    <div class="share">Share on <span class="ico" style="background:#3b5b9a;margin-left:6px"></span><span class="ico" style="background:#3aa4e0"></span></div>
    <a class="btn-more" href="#">View More Details <svg viewBox="0 0 10 10"><circle cx="5" cy="5" r="4.2" fill="none" stroke="#fff"/><path d="M4 3l2 2-2 2" fill="none" stroke="#fff"/></svg></a>
  </article>

  <article class="listing abs" style="top:504px">
    <div class="thumbs">
      <div class="thumb" role="img" aria-label="Parts photo" style="background:linear-gradient(#ddd,#444 55%,#bbb)"></div>
      <div class="thumb" role="img" aria-label="Gyrocopter photo" style="background:linear-gradient(#999,#e8d020 55%,#556)"></div>
      <div class="thumb" role="img" aria-label="Aircraft photo" style="background:linear-gradient(#b9c9d6,#b22 55%,#7a8a55)"></div>
    </div>
    <h2>Norrvinge NV-12</h2>
    <p class="desc">En unik UL-maskin i kolfiber, det gör den exceptionellt lätt. Tomvikt 68kg Tillv. 2006, ca.260 timmar, alltid hangar....</p>
    <dl class="meta"><dt>Namn:</dt> <dd>Nils Berglund</dd><br><dt>Telefon:</dt> <dd>+46 700 00 12 34</dd><br><dt>Datum:</dt> <dd>2013-10-04 16:49:39</dd></dl>
    <div class="share">Share on <span class="ico" style="background:#3b5b9a;margin-left:6px"></span><span class="ico" style="background:#3aa4e0"></span></div>
    <a class="btn-more" href="#">View More Details <svg viewBox="0 0 10 10"><circle cx="5" cy="5" r="4.2" fill="none" stroke="#fff"/><path d="M4 3l2 2-2 2" fill="none" stroke="#fff"/></svg></a>
  </article>

  <article class="listing abs" style="top:649px">
    <div class="thumbs">
      <div class="thumb" role="img" aria-label="Aircraft photo" style="background:linear-gradient(#a9c0d8,#ddd 50%,#3c4a8a 70%,#777)"></div>
      <div class="thumb" role="img" aria-label="Instrument panel photo" style="background:linear-gradient(#888,#333 50%,#999)"></div>
      <div class="thumb" role="img" aria-label="Engine photo" style="background:linear-gradient(#bbb,#555 50%,#aaa)"></div>
    </div>
    <h2>Norrvinge NV-12</h2>
    <p class="desc">En unik UL-maskin i kolfiber, det gör den exceptionellt lätt. Tomvikt 68kg Tillv. 2006, ca.260 timmar, alltid hangar....</p>
    <dl class="meta"><dt>Namn:</dt> <dd>Nils Berglund</dd><br><dt>Telefon:</dt> <dd>+46 700 00 12 34</dd><br><dt>Datum:</dt> <dd>2013-10-04 16:49:39</dd></dl>
    <div class="share">Share on <span class="ico" style="background:#3b5b9a;margin-left:6px"></span><span class="ico" style="background:#3aa4e0"></span></div>
    <a class="btn-more" href="#">View More Details <svg viewBox="0 0 10 10"><circle cx="5" cy="5" r="4.2" fill="none" stroke="#fff"/><path d="M4 3l2 2-2 2" fill="none" stroke="#fff"/></svg></a>
  </article>

  <article class="listing abs" style="top:794px">
    <div class="thumbs">
      <div class="thumb" role="img" aria-label="Aircraft photo" style="background:linear-gradient(#c9d3dc,#c33 55%,#7c9a55)"></div>
      <div class="thumb" role="img" aria-label="Aircraft photo" style="background:linear-gradient(#5d9ad8,#e08a20 55%,#6f8a45)"></div>
      <div class="thumb" role="img" aria-label="Hangar photo" style="background:linear-gradient(#b89a70,#6a4a30 55%,#a88a60)"></div>
    </div>
    <h2>Norrvinge NV-12</h2>
    <p class="desc">En unik UL-maskin i kolfiber, det gör den exceptionellt lätt. Tomvikt 68kg Tillv. 2006, ca.260 timmar, alltid hangar....</p>
    <dl class="meta"><dt>Namn:</dt> <dd>Nils Berglund</dd><br><dt>Telefon:</dt> <dd>+46 700 00 12 34</dd><br><dt>Datum:</dt> <dd>2013-10-04 16:49:39</dd></dl>
    <div class="share">Share on <span class="ico" style="background:#3b5b9a;margin-left:6px"></span><span class="ico" style="background:#3aa4e0"></span></div>
    <a class="btn-more" href="#">View More Details <svg viewBox="0 0 10 10"><circle cx="5" cy="5" r="4.2" fill="none" stroke="#fff"/><path d="M4 3l2 2-2 2" fill="none" stroke="#fff"/></svg></a>
  </article>

  <a class="view-all abs" href="#" style="left:607px;top:938px;flex-direction:row-reverse">
    <svg viewBox="0 0 10 10"><circle cx="5" cy="5" r="4.2" fill="none" stroke="#f26a1b"/><path d="M4 3l2 2-2 2" fill="none" stroke="#f26a1b"/></svg>View All</a>
</main>

<div class="ad abs" style="top:214px;height:271px;background:linear-gradient(#d8dde2,#c9d2db 40%,#8aa0b4)" role="img" aria-label="Aviation finance advertisement"></div>
<div class="ad abs" style="top:494px;height:270px;background:linear-gradient(#e5e5e5,#f4f4f4 50%,#222 93%)" role="img" aria-label="Engine parts advertisement"></div>
<div class="ad abs" style="top:773px;height:136px;background:linear-gradient(#c8262a,#2a3a9a 40%,#4a5ab8 70%,#c8262a)" role="img" aria-label="Aircraft plastics advertisement"></div>

<footer>
  <div class="footer-band abs"></div>
  <div class="footer-panel abs"></div>
  <h4 class="footer-title abs" style="left:120px;top:1005px">Newsletter</h4>
  <p class="footer-text abs" style="left:121px;top:1034px;width:215px">Enjoy the latest Hangar Shop offers and updates. Sign up now &nbsp;and receive 10% off your first order.</p>
  <form class="newsletter-form abs">
    <input type="text" placeholder="Enter email">
    <button type="button"><svg width="18" height="12" viewBox="0 0 18 12"><rect x="0.5" y="0.5" width="17" height="11" fill="#fff" stroke="#fff"/><path d="M1 1l8 6 8-6" fill="none" stroke="#f26a1b"/></svg>Send</button>
  </form>
  <h4 class="footer-title abs" style="left:557px;top:1005px">Quik Links</h4>
  <nav class="quick-links abs"><a href="#">Home</a><a href="#">About Us</a><a href="#">Faq</a><a href="#">Contact Us</a></nav>
  <div class="social abs"><span style="background:#3b5b9a"></span><span style="background:#3aa4e0"></span><span style="background:#0e6aa0"></span></div>
  <div class="footer-rule abs"></div>
  <p class="copyright abs">Copyright © 2013 VINGTORGET . All rights reserved.</p>
</footer>

</body>
</html>
```